Generate website for pollenvault.com

Please design a website for our business. It must be clean, streamlined and obvious.

Our business combines ecommerce, with social networking, and atlaspin maps. The logo is a shopping bag (ecommerce) and honeycombs inside representing the various compartments of business that are offered throughout site.

Clients use our site to visit the interior of stores and restaurants through video streaming and can virtually "walk through" the store and purchase items with friends and loved ones through the web.

We want to incorporate this logo with the work that we are doing and play on this honeycomb theme.

Our business is "pollenvault.com" because we are all about "u"!

Please make homepage with about us tab, contact us form, mission tab, we also want a page with our research links included that bolster the case for our startup.

We will incorporate a small video on the front screen. A homepage like filecrate.net only this time with our pollenvault!

Also include, COMING SOON, on the homepage please.

These are some good templates/example sites of clean and simple but effective: https://ninelane.example/preview www.filecrate.net

We are excited to see your submissions. Currently, a very good and only one designer has posted so far. Let us know!

Please include the TM (trademark) symbol after the logo, the name, and the slogan throughout the website. Thank you!

Put the TM after the LOGO and after the slogan "Position Used to Matter" Osvaldo

Target Market(s)

We will begin with female online shoppers.

Industry/Entity Type

Shopping

Font styles to use
Serif
Sans Serif

Colors
e567a6
fece3e
85cae6

Requirements
Must have
• Clean Look
Simple like Filecrate with simple options "see film" or login/signup.

With browser tabs at the bottom much like filecrate.

1. Shopper when opening Pollenvault.com website will see a simple webpage with a large Pollenvault logo in the center.

2. User will see log-in and password or create account in upper right hand corner of webpage. Mobile device website will be underneath logo.

3.We Prefer a background for webpages adding a softer experience on the the eyes of the user. A photo in the background to show shopretail experience.

4. Clicking on thePollenvault logo will inform users of details and instructions about platform. Example: About, contact, mission, Help etc. Logo will become somewhat like an interactive tool for help and guidance.

5. Pollenvault is currently scouting for it's founding venues. A founding venue will be the first venues to appear to the public on the Pollenvault platform. Founding venues (FV) will inherit a lifetime of the lowest possible rates of 2%* for the duration of it's business. All businesses wishing to participate in the founding venues offer please leave your email address and store name and a representative will get back with you.

*Venues will be subjected to credit card and CoinDrift rates in addition.

Nice to have
• http://www.patentlook.example/patents/US7391058

Must include the link above/visual of this page on the site as well.

```html
<!DOCTYPE html>
<html lang="en">
<head>
<meta charset="utf-8">
<title>Contact · Pollenvault.com</title>
<link href="https://fonts.googleapis.com/css2?family=Belleza&family=Tinos&family=Didact+Gothic&display=swap" rel="stylesheet">
<style>
  :root {
    --ink: #1a1a1a;
    --ink-soft: #3a3530;
    --rule: #2a2a2a;
    --rule-soft: #8c8479;
    --field: #ffffff;
    --field-border: #2b2b2b;
    --gold-top: #e2c34a;
    --gold-mid: #c9a21f;
    --gold-low: #a67d10;
    --button-edge: #f3ecd6;
    --scene-a: #f4ede0;
    --scene-b: #e9d6b0;
    --scene-c: #dcc398;
    --scene-d: #efe6d6;
  }
  * { box-sizing: border-box; margin: 0; padding: 0; }
  html, body { width: 1200px; height: 900px; overflow: hidden; }
  body {
    position: relative;
    font-family: "Belleza", "Trebuchet MS", sans-serif;
    color: var(--ink);
  }
  .store-backdrop {
    position: absolute; inset: 0;
    background:
      radial-gradient(ellipse at 75% 70%, var(--scene-c) 0%, transparent 55%),
      radial-gradient(ellipse at 20% 30%, var(--scene-b) 0%, transparent 50%),
      linear-gradient(160deg, var(--scene-d) 0%, var(--scene-a) 45%, var(--scene-b) 100%);
  }
  .page-title {
    position: absolute; left: 0; width: 1236px; top: 14px;
    text-align: center; font-size: 44px; font-weight: 400; line-height: 1;
  }
  .title-rule {
    position: absolute; left: 48px; top: 73px; width: 1119px; height: 1px;
    background: var(--rule);
  }
  .field-label {
    position: absolute; left: 122px; font-size: 24px; line-height: 1;
  }
  .label-name { top: 106px; }
  .label-email { top: 256px; }
  .label-comments { top: 398px; }
  .field {
    position: absolute; left: 115px; background: var(--field);
    border: 1px solid var(--field-border);
  }
  .field-name { top: 145px; width: 446px; height: 66px; }
  .field-email { top: 292px; width: 446px; height: 67px; }
  .field-comments { top: 436px; width: 539px; height: 295px; }
  .send-button {
    position: absolute; left: 118px; top: 742px; width: 170px; height: 54px;
    border: 2px solid var(--button-edge); border-radius: 3px;
    background: linear-gradient(180deg, var(--gold-top) 0%, var(--gold-mid) 50%, var(--gold-low) 100%);
    color: #ffffff; font-family: "Belleza", "Trebuchet MS", sans-serif; font-size: 23px;
    display: flex; align-items: center; justify-content: center;
    padding-bottom: 4px;
  }
  .photo-credit {
    position: absolute; left: 692px; top: 784px;
    font-family: "Tinos", "Times New Roman", serif; font-size: 20px; color: var(--ink-soft);
    white-space: nowrap;
  }
  .venue-note {
    position: absolute; left: 0; width: 1176px; text-align: center;
    font-family: "Tinos", "Times New Roman", serif; font-size: 18px; line-height: 1;
  }
  .venue-offer { top: 813px; }
  .venue-limit { top: 837px; }
  .footer-rule {
    position: absolute; left: 172px; top: 861px; width: 853px; height: 1px;
    background: var(--rule-soft);
  }
  .legal {
    position: absolute; left: 0; width: 1216px; top: 876px; text-align: center;
    font-family: "Didact Gothic", "Century Gothic", sans-serif; font-size: 14px;
    letter-spacing: 0.1px; color: var(--ink);
  }
</style>
</head>
<body>
  <div class="store-backdrop" role="img" aria-label="Bright multi-level retail store interior seen from above, softly washed out"></div>

  <h1 class="page-title">Contact</h1>
  <div class="title-rule"></div>

  <form class="contact-form">
    <label class="field-label label-name" for="name">Name :</label>
    <input class="field field-name" id="name" type="text">

    <label class="field-label label-email" for="email">Email :</label>
    <input class="field field-email" id="email" type="email">

    <label class="field-label label-comments" for="comments">Comments and collaborations:</label>
    <textarea class="field field-comments" id="comments"></textarea>

    <div class="send-button">Send</div>
  </form>

  <p class="photo-credit">https://www.photoshelf.example/photos/lenamarsh/4172930581</p>

  <p class="venue-note venue-offer">Founding Venues will inherit a 2% lifetime fee*</p>
  <p class="venue-note venue-limit">Limited to a select few</p>

  <div class="footer-rule"></div>
  <p class="legal">©2014 · Pollenvault.com LLC. All Rights Reserved. Under Use and Authority of Uspto Patent# 7391058.</p>
</body>
</html>
```